website in progress for new building development

Hi,
I have a new real estate development website in making but am running out of time for its completion. It's for a new apartment building for sales. Would it be possible for you to change/alter the site according to my requirements? I could send you all the existing files. The bulk of the website is done.
The images aren't really ready yet but will be within the next days so those will need to be replaced. Currently draft images are the placeholder on the website.

Let me know if you would be interested so we can quickly pick up correspondence.

This is the website so far (using Wordpress):
http://lindmoor.com.au/lindmoor/

Our domain is:
lindmoor.com.au

I am also adding the theme I am using.

Thanks.

Target Market(s)

Potential buyers.

Industry/Entity Type

Real Estate Development

Number of Pages Required

5+ page

Font styles to use
Other font styles liked:
• I used Robot under google fonts for the headlines

Requirements
Must have
• This is the current website
• http://lindmoor.com.au/lindmoor
• I'd like the colour scheme to remain the way it is.
• 1. Header
• I would like the header to have the menu on the right and have the 'Reigster' button similar to this website: (see the header here which shows up once you scroll down in the page) http://zenithbyfalconhouse.com.au/
• Please adjust this feature into our website with the menu items given.
• 2. Logo on Homepage
• Add the lindmoor logo into the top center of the feature image.
• Though permanent images are yet to arrive in the next few days. These are only drafts.
• 3. Footer
• Not sure about the colour scheme here yet.
• Should contain Disclaimer and copyrights.
• 4.Pages:
• a) Home
• b) Building
• c) Interior
• d) Location
• e) Register
• 5. page 'Home'
• When you scroll down in lindmoor.com.au/lindmoor/ you see the three images under the feature image, I would like those being hyperlinked as a 'box' just like this website has them when you scroll down here:
• http://www.velmotide.com.au/
• 6. page 'Register'
• I like the subtle colour scheme for the form used here http://zenithbyfalconhouse.com.au/#enquire-now
• and their 'Submit' button. Maybe adjust it to my website and remove the borders in the fields.
• 7. page 'Building'
• Will have two images of the exterior of the building which should be sliding automatically. (Images will be provided soon. For now I am only attaching draft images.)
• 8. page 'Interior'
• Will also have two images of the interior which should be automatically sliding. (Images will be provided soon. Attaching draft images for now)
Nice to have
• A language selection in the top right corner of each page:
• selection between english, mandarin, cantonese, korean.

```html
<!DOCTYPE html>
<html lang="en">
<head>
<meta charset="utf-8">
<title>Lindmoor – Contemporary Parkside Living</title>
<link rel="stylesheet" href="https://fonts.googleapis.com/css2?family=Roboto:wght@300;400;500;700&family=Roboto+Condensed:wght@400;700&display=swap">
<style>
:root{
  --orange:#e8941a;
  --orange-dark:#c97a0e;
  --ink:#333333;
  --text:#5a5a5a;
  --muted:#8a8a8a;
  --line:#d6d6d6;
  --panel:#eeeeee;
  --topbar:#2b2b2b;
  --white:#ffffff;
}
*{box-sizing:border-box;margin:0;padding:0}
html,body{width:1200px;height:2356px;overflow:hidden;background:var(--white)}
body{font-family:"Roboto",Arial,sans-serif;color:var(--text);position:relative}
.page{position:relative;width:1200px;height:2356px;overflow:hidden}

.topbar{position:absolute;top:0;left:0;width:1200px;height:32px;background:var(--topbar);color:#ddd;font-size:14px;display:flex;justify-content:flex-end;align-items:center;gap:28px;padding-right:60px}
.topbar .lang{display:flex;align-items:center;gap:8px}
.topbar .lang::after{content:"";border:5px solid transparent;border-top-color:#ddd;margin-top:5px}

.header{position:absolute;top:32px;left:0;width:1200px;height:176px;background:var(--white);display:flex;align-items:center;justify-content:space-between;padding:0 90px 0 96px}
.brand{display:flex;flex-direction:column;align-items:flex-start;gap:14px}
.brand-mark{width:58px;height:58px;background:var(--orange)}
.brand-name{font-family:"Roboto",sans-serif;font-weight:400;font-size:24px;letter-spacing:6px;color:var(--orange)}
.nav{display:flex;gap:46px;font-family:"Roboto",sans-serif;font-size:30px;color:var(--ink)}
.nav a{color:inherit;text-decoration:none;padding-bottom:14px;border-bottom:3px solid transparent}
.nav a.active{color:var(--orange);border-bottom-color:var(--orange)}

.hero{position:absolute;top:208px;left:0;width:1200px;height:552px;background:linear-gradient(180deg,#b7c3cc 0%,#d9dde0 35%,#a99b8d 62%,#6d6258 85%,#4b4540 100%)}

.intro{position:absolute;top:790px;left:0;width:1200px;text-align:center}
.section-title{font-family:"Roboto Condensed",sans-serif;font-weight:700;font-size:34px;color:var(--ink);letter-spacing:.5px}
.divider{display:flex;align-items:center;justify-content:center;gap:10px;margin:14px auto 0}
.divider span{width:120px;height:1px;background:var(--line)}
.divider i{width:12px;height:12px;border:1px solid var(--muted);transform:rotate(45deg)}
.intro p{font-size:15px;line-height:24px;color:var(--text);margin:0 auto;width:880px}
.intro .lead{margin-top:30px}
.intro .body{margin-top:36px}

.features{position:absolute;top:1130px;left:0;width:1200px;height:462px;background:var(--panel)}
.feature{position:absolute;top:62px;width:308px}
.feature-img{width:308px;height:200px}
.feature h3{font-family:"Roboto Condensed",sans-serif;font-weight:400;font-size:28px;color:var(--ink);text-align:center;margin-top:20px;letter-spacing:1px}
.feature hr{border:0;border-top:1px solid var(--line);margin:6px 0 8px}
.feature p{font-size:14px;line-height:19px;color:var(--text);padding:0 14px}
.feature .bar{height:5px;background:var(--orange);margin-top:14px;width:236px}

.register{position:absolute;top:1592px;left:0;width:1200px;height:488px;background:linear-gradient(180deg,#c9ccd0 0%,#d8d9da 40%,#bfb6ac 100%)}
.register-veil{position:absolute;inset:0;background:rgba(255,255,255,.55)}
.register h2{position:absolute;top:36px;width:1200px;text-align:center}
.contact-card{position:absolute;top:108px;left:60px;width:328px;height:340px;background:var(--white);box-shadow:0 2px 8px rgba(0,0,0,.15);padding:56px 26px 0}
.contact-badge{position:absolute;top:-26px;left:134px;width:60px;height:60px;border-radius:50%;background:var(--orange);color:var(--white);font-family:"Roboto",sans-serif;font-weight:700;font-size:36px;display:flex;align-items:center;justify-content:center}
.contact-card h4{font-family:"Roboto Condensed",sans-serif;font-weight:400;font-size:28px;color:var(--muted);text-align:center;letter-spacing:1px}
.contact-card hr{border:0;border-top:1px solid var(--line);margin:10px 0 18px}
.contact-card .team{font-size:19px;color:var(--ink);font-weight:500}
.contact-card address{font-style:normal;font-size:17px;line-height:23px;color:var(--text)}
.form{position:absolute;top:132px;left:448px;width:712px}
.form .title{font-size:17px;color:var(--ink)}
.field{display:flex;align-items:center;height:42px;margin-top:8px}
.field label{width:112px;white-space:nowrap;font-size:17px;color:var(--text);text-align:right;padding-right:12px}
.field span{flex:0 0 456px;height:34px;background:rgba(255,255,255,.8)}
.submit{position:absolute;top:396px;left:768px;width:248px;height:44px;background:var(--orange-dark);color:var(--white);font-family:"Roboto Condensed",sans-serif;font-size:24px;letter-spacing:1px;display:flex;align-items:center;justify-content:center}

.footer{position:absolute;top:2080px;left:0;width:1200px;height:232px;background:var(--orange);color:var(--white)}
.footer h5{font-family:"Roboto",sans-serif;font-weight:400;font-size:24px;letter-spacing:.5px}
.footer .links{position:absolute;top:20px;left:60px}
.footer .links p{font-size:15px;line-height:20px;margin-top:22px}
.social{display:flex;gap:14px;margin-top:12px}
.social span{width:34px;height:34px;background:var(--white)}
.footer .footer-brand{position:absolute;top:42px;left:540px;width:120px;display:flex;flex-direction:column;align-items:center;gap:14px}
.footer .footer-brand .brand-mark{background:var(--white);width:70px;height:70px}
.footer .footer-brand .brand-name{color:var(--white);font-size:24px}
.footer .hours{position:absolute;top:20px;left:820px}
.footer .hours p{font-size:15px;line-height:20px}
.footer .hotline{margin-top:18px}
.footer .times{margin-top:16px}
.to-top{position:absolute;top:108px;right:36px;width:64px;height:64px;background:var(--orange-dark)}
.copyright{position:absolute;top:2312px;left:0;width:1200px;height:44px;background:var(--orange-dark);color:var(--white);font-size:18px;display:flex;align-items:center;padding-left:24px}
</style>
</head>
<body>
<div class="page">

  <div class="topbar">
    <span>Choose your language</span>
    <span class="lang">English</span>
  </div>

  <header class="header">
    <div class="brand">
      <span class="brand-mark"></span>
      <span class="brand-name">LINDMOOR</span>
    </div>
    <nav class="nav">
      <a class="active">Home</a>
      <a>Building</a>
      <a>Interior</a>
      <a>Location</a>
      <a>Register</a>
    </nav>
  </header>

  <div class="hero" role="img" aria-label="Photo of the apartment building exterior with street and trees in front"></div>

  <section class="intro">
    <h1 class="section-title">CONTEMPORARY PARKSIDE LIVING</h1>
    <div class="divider"><span></span><i></i><span></span></div>
    <p class="lead">Located on a quiet suburban street, The Velmotide is a striking and contemporary boutique development that opens up to the peace and tranquility of the great outdoors.</p>
    <p class="body">Artfully conceived and expertly detailed, The Velmotide is a distinctive and sculptural development of only 21 apartments, perfectly located between iconic Bondi Beach and the unrivalled convenience of Bondi Junction. Orientated towards a landscaped community garden, The Velmotide offers a peaceful setting and a leafy outlook for each of the development's carefully planned lifestyle apartments. Dining, living and bedroom spaces are all oriented towards this valuable, shared amenity, bringing abundant natural light and cross flow ventilation into the apartments' stylish interiors.</p>
  </section>

  <section class="features">
    <article class="feature" style="left:100px">
      <div class="feature-img" role="img" aria-label="Photo of the building exterior" style="background:linear-gradient(180deg,#c7ccd0,#9c948a)"></div>
      <h3>BUILDING</h3><hr>
      <p>Lorem ipsum dolor sit amet, consectetuer adipiscing elit. Aenean commodo ligula eget dolor. Aenean massa.</p>
      <div class="bar"></div>
    </article>
    <article class="feature" style="left:446px">
      <div class="feature-img" role="img" aria-label="Photo of an apartment interior living room" style="background:linear-gradient(180deg,#d8d4cc,#a89c8c)"></div>
      <h3>INTERIOR</h3><hr>
      <p>Lorem ipsum dolor sit amet, consectetuer adipiscing elit. Aenean commodo ligula eget dolor. Aenean massa.</p>
    </article>
    <article class="feature" style="left:796px">
      <div class="feature-img" role="img" aria-label="Photo of the building seen from the street under blue sky" style="background:linear-gradient(180deg,#5d8fc4,#a9c3dc 55%,#8a8f86)"></div>
      <h3>LOCATION</h3><hr>
      <p>Lorem ipsum dolor sit amet, consectetuer adipiscing elit. Aenean commodo ligula eget dolor. Aenean massa.</p>
    </article>
  </section>

  <section class="register" role="img" aria-label="Faded photo of the building as background">
    <div class="register-veil"></div>
    <h2 class="section-title">REGISTER NOW</h2>
    <div class="contact-card">
      <div class="contact-badge">?</div>
      <h4>CONTACT US</h4><hr>
      <p class="team">LINDMOOR TEAM</p>
      <address>(02) 5550 1482<br>12 Harbour Row, Lindfield,<br>Sydney<br>support@lindmoor.com.au</address>
    </div>
    <div class="form">
      <p class="title">Inquire Today</p>
      <div class="field"><label>*Name:</label><span></span></div>
      <div class="field"><label>*Email:</label><span></span></div>
      <div class="field"><label>*Mobile No:</label><span></span></div>
      <div class="field"><label>*Address:</label><span></span></div>
    </div>
    <div class="submit">SUBMIT</div>
  </section>

  <footer class="footer">
    <div class="links">
      <h5>INTERESTING LINKS</h5>
      <p>Below are some interesting links<br>for your trip, enjoy your stay :)</p>
      <div class="social"><span></span><span></span></div>
    </div>
    <div class="footer-brand">
      <span class="brand-mark"></span>
      <span class="brand-name">LINDMOOR</span>
    </div>
    <div class="hours">
      <h5>BUSINESS HOURS</h5>
      <p class="hotline">Our support Hotline is: (02) 5550 1499</p>
      <p class="times">Monday-Friday: 9am to 6pm<br>Saturday: 9am to 2pm<br>Sunday: Closed</p>
    </div>
    <div class="to-top">
      <svg width="64" height="64" viewBox="0 0 64 64"><path d="M20 38 L32 26 L44 38" fill="none" stroke="#fff" stroke-width="4"/></svg>
    </div>
  </footer>
  <div class="copyright">© Copyright - 2015 Lindmoor - All right reserved.</div>

</div>
</body>
</html>
```